依頼詳細
現状、施工した場所に施工済ステッカーを貼っているのですが、
今回施工をしたホテル様の要望で、フロントや客室にお客様へ向けたアピールできるチラシなどが欲しいといわれました。
ホテルのフロント・客室の卓上におけるものや・車内に貼れるものなので
年賀状サイズくらいで検討しています。

イメージは
・主成分でもある青森ヒバをモチーフにしたもの
・一目でわかる安心感が伝わるもの
・100%天然成分で安心安全
・キャッチコピーは『植物の力で抗菌中!』

記載項目
ヴェルトナ産業株式会社 0120-387-905
Lumiva Plus
サイズ
年賀状サイズくらい
ページ数
片面
希望イメージ
シンプル 複雑
単色 カラフル
暗い 明るい
日常 高級
遊び心 厳粛
未来的 伝統的
女性的 男性的
希望する色
緑系、青系
納品ファイル
• 高解像度JPG (.jpg)
補足説明
当社が使用しているチラシです。
■ 選んだ理由

どの候補者もとても良かったですが、
こちらはどのシチュエーションでもあうようなデザインかつ
柔らかい印象で、安心感を与えてくれるようなデザインなので決めました。

■ 提案者全員のお礼・コメント

とても素晴らしいデザインばかりでかなり迷いました。
予算があれば他の候補者も当選sて他のですが。
今後は社のチラシなども作成予定ですので、
またお願いするかと思います。
宜しくお願い致します。

```html
<!DOCTYPE html>
<html lang="ja">
<head>
<meta charset="UTF-8">
<title>植物の力で抗菌中 | Lumiva Plus</title>
<link rel="stylesheet" href="https://fonts.googleapis.com/css2?family=Noto+Sans+JP:wght@400;500;700&family=Roboto:wght@400&display=swap">
<style>
  :root {
    --leaf-deep: #1f4a1c;
    --leaf-mid: #3f7a32;
    --leaf-light: #6fa452;
    --leaf-bright: #8dbb6a;
    --ink-white: #ffffff;
    --tag-fill: rgba(20, 60, 20, 0.35);
  }
  * { margin: 0; padding: 0; box-sizing: border-box; }
  html, body { width: 811px; height: 1200px; overflow: hidden; background: var(--leaf-deep); }
  .flyer {
    position: relative;
    width: 811px;
    height: 1200px;
    overflow: hidden;
    font-family: "Noto Sans JP", sans-serif;
    color: var(--ink-white);
  }
  .foliage-photo {
    position: absolute;
    inset: 0;
    background:
      radial-gradient(ellipse at 30% 25%, var(--leaf-bright) 0%, transparent 45%),
      radial-gradient(ellipse at 75% 70%, var(--leaf-light) 0%, transparent 50%),
      linear-gradient(160deg, var(--leaf-mid) 0%, var(--leaf-deep) 55%, var(--leaf-mid) 100%);
  }
  .frame {
    position: absolute;
    border: 2px solid var(--ink-white);
    pointer-events: none;
  }
  .frame--outer { inset: 19px; }
  .frame--inner { inset: 32px; border-width: 1.5px; }
  .text-block {
    position: absolute;
    left: 0; right: 0;
    text-align: center;
    text-shadow: 0 2px 8px rgba(0, 0, 0, 0.35);
  }
  .catch-lead { top: 350px; font-size: 62px; font-weight: 500; letter-spacing: 0.04em; }
  .catch-main { top: 470px; font-size: 116px; font-weight: 500; letter-spacing: 0.08em; }
  .product-name { top: 700px; font-family: "Roboto", sans-serif; font-size: 42px; font-weight: 400; letter-spacing: 0.02em; }
  .ingredients {
    position: absolute;
    top: 792px; left: 0; right: 0;
    display: flex;
    justify-content: center;
    gap: 12px;
    list-style: none;
  }
  .ingredient-tag {
    border: 1.5px solid var(--ink-white);
    background: var(--tag-fill);
    font-size: 20px;
    line-height: 1;
    padding: 6px 12px;
  }
  .natural-badge {
    position: absolute;
    top: 850px; left: 50%;
    transform: translateX(-50%);
    border: 2px solid var(--ink-white);
    background: var(--tag-fill);
    font-size: 29px;
    font-weight: 500;
    line-height: 1;
    padding: 8px 26px;
    white-space: nowrap;
  }
  .company-line {
    position: absolute;
    bottom: 90px; left: 0; right: 0;
    text-align: center;
    font-size: 20px;
    letter-spacing: 0.04em;
    text-shadow: 0 1px 4px rgba(0, 0, 0, 0.4);
  }
  .company-line .phone { margin-left: 18px; }
</style>
</head>
<body>
<main class="flyer">
  <div class="foliage-photo" role="img" aria-label="青森ヒバの緑の葉が画面いっぱいに広がる写真"></div>
  <div class="frame frame--outer"></div>
  <div class="frame frame--inner"></div>

  <h1 class="text-block catch-lead">植物の力で</h1>
  <p class="text-block catch-main">抗菌中</p>
  <p class="text-block product-name">Lumiva Plus</p>

  <ul class="ingredients">
    <li class="ingredient-tag">青森ヒバ</li>
    <li class="ingredient-tag">ヒノキ</li>
    <li class="ingredient-tag">ティーツリー</li>
  </ul>
  <p class="natural-badge">100%天然成分</p>

  <p class="company-line">ヴェルトナ産業株式会社<span class="phone">0120-387-905</span></p>
</main>
</body>
</html>
```